Commercial Real Estate Flyer

We are looking to get a real estate flyer done for our office space. It will be multiple pages including
1) Overview of the building with amenities
2) A map showing the building and restaurants near by with pins and logos
3) Demographics of the population surrounding

I have attached an example

Target Market(s)

People needing an executive office, virtual office, coworking or a meeting room

Industry/Entity Type

Real Estate

Requirements
Must have
• Be able to be emailed in a campaign using something like mail chimp
• Using the colors from our logo: www.tremvolux.com
Nice to have
• MB's kept low

```html
<!DOCTYPE html>
<html lang="en">
<head>
<meta charset="utf-8">
<title>Office Building For Sale – Flyer</title>
<link href="https://fonts.googleapis.com/css2?family=Oswald:wght@600;700&family=Roboto+Condensed:wght@400;500&family=Lato:wght@400&display=swap" rel="stylesheet">
<style>
  :root{
    --green:#6cc24a;
    --green-dark:#4f9a2f;
    --green-mid:#5cb13b;
    --ink:#2b2b2b;
    --cell-dark:#232323;
    --cell-gray:#9a9a9a;
    --paper:#ffffff;
    --backdrop:#e9e9e9;
  }
  html,body{margin:0;padding:0;width:1200px;height:1200px;overflow:hidden;background:var(--backdrop);}
  .stage{position:absolute;left:0;top:0;width:1500px;height:1500px;transform:scale(0.8);transform-origin:0 0;}
  .page{position:absolute;top:207px;width:660px;height:926px;background:var(--paper);overflow:hidden;}
  .page--cover{left:68px;}
  .page--details{left:773px;}
  .page-art{position:absolute;left:0;top:0;width:660px;height:926px;}

  /* cover */
  .cover-title{position:absolute;left:23px;top:552px;margin:0;font-family:"Oswald",sans-serif;font-weight:700;color:var(--ink);line-height:1;}
  .cover-title .kicker{display:block;font-size:29px;line-height:38px;letter-spacing:.3px;}
  .cover-title .type{display:block;font-size:38px;line-height:48px;color:var(--green);margin-top:4px;}
  .cover-title .sale{display:block;font-family:"Roboto Condensed",sans-serif;font-weight:500;font-size:94px;line-height:90px;letter-spacing:-1px;margin-top:2px;}
  .brand-name{position:absolute;left:446px;top:596px;font-family:"Lato",sans-serif;font-weight:400;font-size:33px;color:#fff;letter-spacing:.5px;}
  .cover-url{position:absolute;left:25px;top:886px;font-family:"Lato",sans-serif;font-size:12.5px;letter-spacing:3px;color:var(--ink);}
  .cover-note{position:absolute;left:329px;top:872px;width:320px;margin:0;font-family:"Roboto Condensed",sans-serif;font-weight:400;font-size:10.5px;line-height:14px;color:var(--ink);}

  /* details */
  .section-head{position:absolute;left:23px;top:18px;width:637px;display:flex;align-items:flex-end;}
  .section-head h2{margin:0;font-family:"Oswald",sans-serif;font-weight:600;font-size:27px;line-height:34px;color:var(--green);white-space:nowrap;}
  .section-head .rule{flex:1;height:2px;background:var(--green);margin:0 0 7px 8px;}
  .highlights{position:absolute;left:24px;top:60px;width:620px;margin:0;padding:0;list-style:none;font-family:"Lato",sans-serif;font-size:11.6px;line-height:14px;color:var(--ink);}
  .highlights li{position:relative;padding-left:20px;margin-bottom:14.5px;}
  .highlights li::before{content:"";position:absolute;left:1px;top:4px;width:6px;height:6px;border-radius:50%;background:var(--green);}
  .facts{position:absolute;left:25px;top:252px;border-collapse:separate;border-spacing:3px;margin:-3px;font-family:"Lato",sans-serif;font-size:11.8px;color:#fff;}
  .facts td{width:150px;height:36px;text-align:center;line-height:13px;padding:0 4px;box-sizing:border-box;}
  .facts .d{background:var(--cell-dark);}
  .facts .g{background:var(--cell-gray);}
</style>
</head>
<body>
<div class="stage">

  <section class="page page--cover">
    <svg class="page-art" viewBox="0 0 660 926">
      <defs>
        <linearGradient id="lobby" x1="0" y1="0" x2="0" y2="1">
          <stop offset="0" stop-color="#8a7a6c"/>
          <stop offset=".18" stop-color="#ece9e4"/>
          <stop offset=".45" stop-color="#dcd8d2"/>
          <stop offset=".7" stop-color="#c9a397"/>
          <stop offset="1" stop-color="#cfc8be"/>
        </linearGradient>
        <linearGradient id="facade" x1="1" y1="0.3" x2="0" y2="1">
          <stop offset="0" stop-color="#c8c8c8"/>
          <stop offset=".6" stop-color="#ececec"/>
          <stop offset="1" stop-color="#ffffff" stop-opacity="0"/>
        </linearGradient>
      </defs>
      <rect role="img" aria-label="Photo of the bright office lobby with red leather armchairs" x="0" y="0" width="660" height="640" fill="url(#lobby)"/>
      <polygon fill="var(--green)" points="0,363 440,600 660,470 660,740 0,440"/>
      <polygon fill="var(--green-dark)" opacity=".55" points="0,363 50,390 50,420 0,400"/>
      <polygon fill="var(--green-dark)" opacity=".45" points="130,440 210,480 130,500"/>
      <polygon fill="var(--green-dark)" opacity=".5" points="290,520 375,500 375,575"/>
      <polygon fill="var(--green-mid)" opacity=".6" points="375,575 440,600 480,575"/>
      <polygon fill="var(--paper)" points="0,440 660,740 660,926 0,926"/>
      <polygon role="img" aria-label="Faded photo of the white office building exterior" fill="url(#facade)" points="300,926 660,926 660,735 470,660 300,760"/>
      <polygon fill="var(--green)" points="0,783 95,835 292,926 0,926"/>
      <line x1="0" y1="892" x2="100" y2="836" stroke="#fff" stroke-width="3"/>
    </svg>
    <h1 class="cover-title">
      <span class="kicker">IDEAL</span>
      <span class="kicker">OWNER/USER</span>
      <span class="type">OFFICE BUILDING</span>
      <span class="sale">FOR SALE</span>
    </h1>
    <div class="brand-name">TREMVOLUX</div>
    <div class="cover-url">www.tremvolux.com</div>
    <p class="cover-note">Tremvolux Provides Class “A” Business Accommodations For Startups, Freelancers, Entrepreneurs &amp; Small Business Owners</p>
  </section>

  <section class="page page--details">
    <svg class="page-art" viewBox="0 0 660 926">
      <defs>
        <linearGradient id="exterior" x1="0" y1="0" x2="0" y2="1">
          <stop offset="0" stop-color="#8fae7a"/>
          <stop offset=".25" stop-color="#b8d2e6"/>
          <stop offset=".45" stop-color="#eeebe4"/>
          <stop offset=".72" stop-color="#d9d3c8"/>
          <stop offset="1" stop-color="#8a8482"/>
        </linearGradient>
        <linearGradient id="topfade" x1="0" y1="0" x2="1" y2="0">
          <stop offset="0" stop-color="#fff" stop-opacity="0"/>
          <stop offset="1" stop-color="#fff" stop-opacity=".7"/>
        </linearGradient>
      </defs>
      <polygon fill="var(--green)" points="0,410 660,515 660,530 0,424"/>
      <polygon role="img" aria-label="Photo of the white stucco office building with iron gate and parking lot" fill="url(#exterior)" points="0,424 660,530 660,926 0,926"/>
    </svg>
    <div class="section-head"><h2>PROPERTY HIGHLIGHTS</h2><span class="rule"></span></div>
    <ul class="highlights">
      <li>Outstanding visibility on Cedarline Road frontage (18,227 VPD) with excellent monument signage</li>
      <li>Superior location three blocks from the Larkfield Square Shopping Center featuring an amazing mix of retail stores and restaurants including Harvest Lane Market, Meadowgrain Bakery and PawHaven.</li>
      <li>Ample parking 30 stalls (est)</li>
      <li>Easy access to Loop 48, US-12, and I-7</li>
      <li>Bonus! New owner has ability to keep existing income in place and expand as needed</li>
      <li>Adjacent Land is Available For Sale (.86 AC)</li>
    </ul>
    <table class="facts">
      <tr><td class="g">Sale Type:</td><td class="g">Investment or<br>Owner/User</td><td class="d">Building 1619:</td><td class="d">±4,100 SF</td></tr>
      <tr><td class="d">Sale Price:</td><td class="d">$699,900</td><td class="g">Lot Size:</td><td class="g">0.52 Acres</td></tr>
      <tr><td class="g">Total Building Size:</td><td class="g">± 6,400 SF</td><td class="d">Year Built:</td><td class="d">1986</td></tr>
      <tr><td class="d">Building 1615:</td><td class="d">±2,300 SF</td><td class="g">Zoning:</td><td class="g">C-T</td></tr>
    </table>
  </section>

</div>
</body>
</html>
```